Interimsmanager sucht Design
Zielgruppe
Erbringen von Dienstleistungen in Form Interimsmanagement in Krankenhäusern in den Bereichen IT, Medizintechnik, Projektmanagement
Zielgruppe: Vorstände, Bereichsleiter, Entscheider für IT und Medizintechnik und Kosten
Branchen: Krankenhäuser, IT, Dienstleistung
Aufgabenstellung
1) Flyer DIN A 4 6seitig (2-Bruch-Wickel-Falz)
2) Texte und grobe Layout-Vorgabe in anhängendem PDF (siehe auch 6)
3) erforderliche Fotos z.B. aus Portalen wie Bildora Platzhalter/Preview einsetzen, die Lizenzen werden dann von mir gekauft
4) Alternativ-Vorschläge bei Bildauswahl willkommen
5) 1 Profilbild je nach Platz/Layout einbauen
6) Logo-Vorlage in diversen Formaten, kann auch noch für 300dpi aufbereitet werden (derzeit noch nicht vorhanden)
6) anhängendes Dokument gibt nur grob vor, wie so etwas aussehen könnte - Alternativ-Vorschläge willkommen

```html
<!DOCTYPE html>
<html lang="de">
<head>
<meta charset="utf-8">
<title>Ardelwin Business – Flyer</title>
<link href="https://fonts.googleapis.com/css2?family=Roboto:ital,wght@0,300;0,400;0,700;0,900;1,400&display=swap" rel="stylesheet">
<style>
  :root {
    --brand-blue: #17597c;
    --brand-navy: #0f4f78;
    --accent-blue: #2f9fd8;
    --text-grey: #555b60;
    --panel-grey: #ececec;
    --white: #ffffff;
    --muted: #8c8a86;
    --ink: #222222;
  }
  * { margin: 0; padding: 0; box-sizing: border-box; }
  html, body { width: 1200px; height: 933px; overflow: hidden; background: var(--white); }
  body { font-family: "Roboto", Arial, sans-serif; position: relative; }

  .flyer { position: relative; width: 1200px; height: 933px; }
  .panel { position: absolute; top: 0; height: 933px; }

  /* Left panel */
  .panel--intro { left: 0; width: 402px; background: var(--white); }
  .portrait {
    position: absolute; left: 0; top: 0; width: 402px; height: 305px;
    background: linear-gradient(135deg, #e9e9e9 0%, #cfcfcf 55%, #8d8d8d 100%);
  }
  .title-band {
    position: absolute; left: 0; top: 188px; width: 402px; height: 117px;
    background: var(--brand-blue);
  }
  .title {
    position: absolute; left: 42px; top: 196px;
    color: var(--white); font-weight: 300; font-size: 50px; line-height: 50px;
  }
  .intro-text {
    position: absolute; left: 42px; top: 326px; width: 340px;
    color: var(--accent-blue); font-style: italic; font-size: 14.5px; line-height: 20px;
  }
  .intro-text p + p { margin-top: 14px; }
  .contact-person {
    position: absolute; left: 42px; top: 426px;
    color: var(--brand-navy); font-weight: 700; font-size: 13.5px;
  }
  .qualifications {
    position: absolute; left: 42px; top: 466px; width: 350px;
    list-style: none; color: var(--text-grey); font-size: 13px; line-height: 21px;
  }
  .qualifications li { padding-left: 12px; position: relative; }
  .qualifications li::before { content: "•"; position: absolute; left: 0; }
  .quote-mark {
    position: absolute; color: var(--brand-navy); font-weight: 900;
    font-size: 80px; line-height: 80px; font-style: italic;
  }
  .quote-mark--open { left: 24px; top: 574px; }
  .quote-mark--close { left: 326px; top: 650px; }
  .quote {
    position: absolute; left: 62px; top: 607px; width: 320px;
    color: var(--accent-blue); font-style: italic; font-size: 18px; line-height: 22px;
  }
  .references-title {
    position: absolute; left: 0; width: 402px; top: 720px; text-align: center;
    color: var(--brand-navy); font-weight: 700; font-size: 13px;
  }
  .reference {
    position: absolute; width: 170px; text-align: center;
    color: var(--ink); font-weight: 900; font-size: 18px; letter-spacing: 1px; text-transform: uppercase;
  }

  /* Middle panel */
  .panel--contact { left: 402px; width: 393px; background: var(--panel-grey); text-align: center; }
  .contact-heading {
    position: absolute; left: 0; width: 393px; top: 184px;
    color: var(--brand-blue); font-weight: 300; font-size: 52px; letter-spacing: 2px;
  }
  .phone-circle {
    position: absolute; left: 68px; top: 277px; width: 256px; height: 256px;
    border-radius: 50%; background: var(--brand-navy); color: var(--white);
  }
  .phone-circle .label { position: absolute; left: 0; width: 256px; top: 101px; font-weight: 700; font-size: 36px; }
  .phone-circle .number { position: absolute; left: 0; width: 256px; top: 152px; font-weight: 700; font-size: 23px; }
  .partner-label {
    position: absolute; left: 0; width: 393px; top: 676px;
    color: var(--brand-navy); font-weight: 700; font-size: 12px;
  }
  .address {
    position: absolute; left: 0; width: 393px; top: 756px;
    color: var(--brand-navy); font-size: 16.5px; line-height: 22.5px; font-style: normal;
  }

  /* Right panel */
  .panel--services {
    left: 795px; width: 405px;
    background: linear-gradient(120deg, #f3ece4 0%, #ead8c3 40%, #dcb990 70%, #c9d7a4 90%, #b6cf80 100%);
  }
  .lobby-photo {
    position: absolute; left: 52px; top: 128px; width: 296px; height: 300px;
    background: linear-gradient(180deg, #f1f1f1 0%, #dcdcdc 60%, #c4c4c4 100%);
  }
  .photo-frame-base {
    position: absolute; left: 52px; top: 428px; width: 296px; height: 152px; background: var(--white);
  }
  .services-kicker {
    position: absolute; left: 0; width: 405px; top: 678px; text-align: center;
    color: var(--muted); font-weight: 300; font-size: 24px;
  }
  .services {
    position: absolute; left: 0; width: 405px; top: 748px; text-align: center;
    color: var(--brand-navy); font-weight: 700; font-size: 22px; line-height: 37px;
  }
</style>
</head>
<body>
<main class="flyer">

  <section class="panel panel--intro">
    <div class="portrait" role="img" aria-label="Schwarzweiß-Porträtfoto des Ansprechpartners"></div>
    <div class="title-band"></div>
    <h1 class="title">Ardelwin<br>Business –</h1>

    <div class="intro-text">
      <p>Ihr durchsetzungsstarker und erfahrener Spezialist für alle Fragen rund um Medizin-IT und Medizintechnik</p>
      <p>Innovation und Kompetenz für die klinische Praxis</p>
    </div>

    <p class="contact-person">Ihr Ansprechpartner: Dr. Bernhard Lemmer</p>

    <ul class="qualifications">
      <li>Facharzt für Orthopädie</li>
      <li>Medizininformatiker</li>
      <li>Mit über 20 Jahren Expertise in der Medizintechnik und Medizininformatik und im Projektmanagement</li>
      <li>Interdisziplinäre Betrachtung Ihrer Geschäftsprozess</li>
    </ul>

    <span class="quote-mark quote-mark--open">"</span>
    <p class="quote">Lorem ipsum dolor sit amet, consectetuer adipiscing elit, sed diam nonummy nibh.</p>
    <span class="quote-mark quote-mark--close">"</span>

    <h2 class="references-title">Auszug aus unseren Referenzen</h2>
    <p class="reference" style="left:27px; top:762px;">Quenholt</p>
    <p class="reference" style="left:205px; top:762px;">Brastel</p>
    <p class="reference" style="left:27px; top:852px;">Ferlinde</p>
    <p class="reference" style="left:205px; top:852px;">Tovanta</p>
  </section>

  <section class="panel panel--contact">
    <h2 class="contact-heading">KONTAKT</h2>
    <div class="phone-circle">
      <span class="label">Rufnummer</span>
      <span class="number">0821/5927340</span>
    </div>
    <p class="partner-label">Ihr B2B Partner</p>
    <address class="address">
      Lindenstr. 14<br>
      Tel. 0821/5927340<br>
      Fax 0821/5927340<br>
      E-Mail info@ardelwin.de<br>
      Internet www.ardelwin.de
    </address>
  </section>

  <section class="panel panel--services" role="img" aria-label="Unscharfes Foto eines hellen Klinikfoyers mit Pflanzen">
    <div class="lobby-photo" role="img" aria-label="Foto eines hellen Empfangsbereichs mit Pflanzschale"></div>
    <div class="photo-frame-base"></div>
    <p class="services-kicker">Ihr B2B Partner</p>
    <p class="services">Interimsmanagement &amp;<br>Projektmanagement<br>für IT &amp; Med.Technik</p>
  </section>

</main>
</body>
</html>
```